Visitenkarten für Mentorin für Frauen
Zielgruppe
Ich bin Mentorin für Frauen (30-50 Jahre alt), die ihre Berufung endlich finden möchten und sich nach mehr Energie und Sinn sehnen. Ich helfe ihnen mit meiner (Name fehtl noch)-Methode ihren Seelenweg zu finden und zu gehen, sodass sie vor Energie übersprudeln und mit einem Leuchten in den Augen ein Leben in Fluss und Fülle kreieren.
Sie sind nicht unglücklich, aber es fehtl ihnen was, das sie wirklich erfüllt.
Stichwörter: Numerologie, Human Design, Seelenweg, Berufung, Lebensaufgabe, erfüllt sein- endlich die Leere füllen, Freiheit, Selbstbestimmt, Selbstliebe, Potentialentfaltung, Transformation
meine core story:
Mit Freude, unglaublicher Energie und einem Strahlen in den Augen schon vor dem Wecker aufzustehen, war für mich früher undenkbar. Ich konnte mir nicht vorstellen, wie sich Leute auf den Montag freuen konnten.
Dabei hätte mich nicht als unglücklich bezeichnet, aber es fehlt einfach etwas, ich hatte eine innere Leere und eine Sehnsucht nach dem Sinn in meinem Lebe, wollte so geliebt werden wie ich bin und mich auch so zeigen können. Ich weiß wie es ist sich klein, unsicher zu fühlen und nicht zu wissen woher das kommt. Ich habe es einfach nicht für möglich gehalten, dass diese innere Leere so leicht zu füllen ist und Freude, Spaß, Selbstbewusstseein und Leichtigkeit in allen Bereichen mit sich bringt.
Weil ich selbst diesen Weg gegangen bin und weil ich weiß, dass es nichts erfüllenderes gibt als das schlummernde Potential zu erwecken, begleite ich Frauen dabei ihren Seelenweg zu finden und zu gehen.
Dadurch dass sie genau wissen, was ihre Gaben sind und was ihre Seele glücklich macht, haben sie Spaß und Freude, gerade auch in den alltäglichen Dingen. Sie führen ein selbstbestimmtes Leben, lieben sich selbst und zeigen sich so wie sie sind.Die gigantische Energie die dadurch in ihnen frei wird, lässt sie die bisherigen Grenzen überwinden. Sie tun was sie erfüllt, o..
Aufgabenstellung
weiblich, geschwungen, weich: beinhalten solls:
Helena Wortmann
Mentorin für Powerfrauen
(Lebe deine Berufung)--> da bin ich mir nicht ganz sicher ob das gut aussehn wird oder zuviel wird
falls relevant habe ich bisher folgende Schriftarten verwendet: Canva Sans und Tan mon cheri
ist aber kein muss

```html
<!DOCTYPE html>
<html lang="de">
<head>
<meta charset="utf-8">
<title>Helena Wortmann – Visitenkarte</title>
<link rel="stylesheet" href="https://fonts.googleapis.com/css2?family=Bodoni+Moda:wght@400;500&display=swap">
<style>
  :root {
    --paper: #f3efeb;
    --gold: #b4834b;
    --blush: #f7dbd5;
    --rose: #f4c4c2;
    --blush-faint: #f4e3df;
    --speckle: #efc9c2;
  }
  html, body {
    margin: 0;
    padding: 0;
    width: 1200px;
    height: 686px;
    overflow: hidden;
    background: var(--paper);
  }
  .card {
    position: relative;
    width: 1200px;
    height: 686px;
    background: var(--paper);
    overflow: hidden;
  }
  .backdrop {
    position: absolute;
    inset: 0;
    width: 1200px;
    height: 686px;
  }
  .illustration {
    position: absolute;
    border-radius: 50%;
  }
  .butterfly-left {
    left: 112px;
    top: 82px;
    width: 208px;
    height: 204px;
    background: radial-gradient(ellipse at center, rgba(180,131,75,0.28) 0%, rgba(180,131,75,0.10) 60%, rgba(180,131,75,0) 75%);
  }
  .butterfly-right {
    left: 756px;
    top: 396px;
    width: 342px;
    height: 204px;
    background: radial-gradient(ellipse at center, rgba(180,131,75,0.26) 0%, rgba(180,131,75,0.10) 60%, rgba(180,131,75,0) 75%);
  }
  .speckles-top {
    left: 852px;
    top: 76px;
    width: 262px;
    height: 232px;
    background: radial-gradient(ellipse at center, rgba(239,201,194,0.55) 0%, rgba(239,201,194,0) 70%);
  }
  .speckles-bottom {
    left: 114px;
    top: 470px;
    width: 228px;
    height: 170px;
    background: radial-gradient(ellipse at center, rgba(239,201,194,0.5) 0%, rgba(239,201,194,0) 70%);
  }
  .identity {
    position: absolute;
    left: 0;
    right: 0;
    top: 296px;
    text-align: center;
    color: var(--gold);
    font-family: "Bodoni Moda", "Didot", serif;
  }
  .identity__name {
    margin: 0 0 0 44px;
    font-size: 78px;
    font-weight: 500;
    line-height: 1;
    letter-spacing: -0.01em;
    text-transform: uppercase;
  }
  .identity__motto {
    margin: 40px 0 0 28px;
    font-size: 44px;
    font-weight: 400;
    line-height: 1.36;
    letter-spacing: 0.42em;
    text-transform: uppercase;
  }
  .identity__motto span {
    display: block;
  }
</style>
</head>
<body>
  <main class="card">
    <svg class="backdrop" viewBox="0 0 1200 686" aria-hidden="true">
      <path class="blob blob--top-left" fill="var(--blush)"
        d="M150 96 C220 62 320 72 372 110 C410 136 380 170 402 200 C430 240 420 300 380 340 C340 390 260 412 190 396 C120 380 86 320 86 250 C86 180 100 120 150 96 Z"/>
      <path class="blob-line" fill="none" stroke="#fbf1ee" stroke-width="2"
        d="M380 150 C372 200 376 250 372 300 M130 375 C190 410 280 410 330 380"/>
      <path class="blob blob--rose" fill="var(--rose)"
        d="M965 362 C1010 340 1080 345 1094 380 C1106 410 1080 450 1040 472 C1000 492 950 488 940 455 C930 420 930 380 965 362 Z"/>
      <path class="blob blob--faint" fill="var(--blush-faint)"
        d="M1030 462 C1070 452 1100 470 1098 500 C1096 528 1060 536 1035 522 C1010 508 1005 470 1030 462 Z"/>
      <path class="blob blob--blush" fill="var(--blush)" opacity="0.95"
        d="M800 468 C850 452 930 458 954 496 C975 530 950 580 900 592 C850 602 790 590 775 556 C760 520 765 480 800 468 Z"/>
    </svg>

    <div class="illustration speckles-top" role="img" aria-label="Verstreute rosa Punkte als zartes Streumuster"></div>
    <div class="illustration speckles-bottom" role="img" aria-label="Verstreute rosa Punkte als zartes Streumuster"></div>
    <div class="illustration butterfly-left" role="img" aria-label="Goldene Linienzeichnung eines Schmetterlings im Profil"></div>
    <div class="illustration butterfly-right" role="img" aria-label="Goldene Linienzeichnung eines Schmetterlings mit ausgebreiteten Flügeln"></div>

    <section class="identity">
      <h1 class="identity__name">Helena Wortmann</h1>
      <p class="identity__motto"><span>Lebe deine</span><span>Berufung</span></p>
    </section>
  </main>
</body>
</html>
```